Web Site Design

We need to design the whole web site for our small start up. We sell hospitality and culinary art internships abroad. I did my own design with WIX which is horrible meanwhile I started with my business. You can see it www.brindle-passage.org I will need you to create a new and attractive web site and to leave it working on wix. The internship destinations are United Arab Emirates, Thailand, China, Spain, Brazil and maybe leave a couple of pages for future destinations.You could also get other ideas of other sites that do internships.

Target Market(s)

Students and recent graduates of hospitality and culinary art majors

Industry/Entity Type

Education

Number of Pages Required

5+ page

Requirements
Must have
• Addittional to our program destinations, or to the pages in the current site. The website must contain a page for Universities or Hotels who require our service

```html
<!DOCTYPE html>
<html lang="en">
<head>
<meta charset="utf-8">
<title>Brindle Passage – Hospitality Internship Program</title>
<link href="https://fonts.googleapis.com/css2?family=Roboto+Slab:wght@400;700&family=Roboto:wght@400;500;700&family=Open+Sans:wght@400;600&display=swap" rel="stylesheet">
<style>
:root{
  --teal:#1c6e72;
  --teal-dark:#155a5e;
  --navy:#0e2444;
  --ink:#1d1d1d;
  --muted:#555;
  --white:#fff;
}
*{box-sizing:border-box;margin:0;padding:0}
html,body{width:1200px;height:4891px;overflow:hidden}
body{font-family:"Open Sans",Arial,sans-serif;color:var(--ink);background:#fff;position:relative}
section,header,footer{position:absolute;left:0;width:1200px;overflow:hidden}
.abs{position:absolute}
.slab{font-family:"Roboto Slab",Georgia,serif}
.btn{display:inline-block;background:var(--teal);color:#fff;border-radius:30px;font-family:"Roboto",Arial,sans-serif}

/* hero */
.hero{top:0;height:605px;background:linear-gradient(180deg,#3a3a3a 0%,#5d5d5d 45%,#8a8a8a 100%)}
.hero-photo{position:absolute;inset:0;background:radial-gradient(ellipse at 50% 40%,rgba(220,200,180,.35),rgba(30,30,30,.5))}
.brand{left:92px;top:34px;display:flex;align-items:center;gap:12px;color:#fff;font-family:"Roboto",sans-serif;font-size:27px;line-height:1}
.brand-mark{width:56px;height:56px;border:3px solid #fff;border-radius:50%}
.nav{right:90px;top:46px;display:flex;gap:30px;color:#fff;font-family:"Roboto",sans-serif;font-size:19px}
.hero-title{top:246px;width:100%;text-align:center;color:#fff;font-size:48px;font-weight:700}
.hero-sub{top:322px;width:100%;text-align:center;color:#fff;font-family:"Roboto",sans-serif;font-size:31px}
.hero-btn{left:488px;top:390px;width:225px;height:50px;line-height:50px;text-align:center;font-size:22px;background:#2a8a86}

/* about */
.about{top:605px;height:455px;background:#fff}
.about h2{left:126px;top:66px;font-size:35px;line-height:1.25;font-weight:700}
.about h2 span{color:var(--teal);display:block}
.about p{left:126px;top:168px;width:600px;font-size:15px;line-height:26px;color:var(--muted)}
.about .btn{left:132px;top:362px;width:118px;height:32px;line-height:32px;text-align:center;font-size:15px}
.about-photo{left:760px;top:0;width:440px;height:455px;background:linear-gradient(135deg,#c9a36a,#8c7a66 50%,#2d3440)}

/* video */
.video{top:1060px;height:465px;background:linear-gradient(180deg,#cfe0ee 0%,#9fb9cf 35%,#5f7d93 60%,#2f6f8a 100%)}
.play{left:560px;top:172px}

/* shared section title */
.section-title{width:100%;text-align:center;font-size:44px;font-weight:400}

/* destinations */
.destinations{top:1525px;height:605px}
.destinations .section-title{top:98px}
.dest{top:215px;width:245px;text-align:center}
.dest .ph{height:205px;box-shadow:0 4px 10px rgba(0,0,0,.25)}
.dest .lbl{margin-top:28px;font-family:"Roboto",sans-serif;font-size:24px}

/* events */
.events{top:2130px;height:590px;background:linear-gradient(180deg,#1c6a70,#1e7a7c 60%,#17676b)}
.events .section-title{top:56px;color:#fff}
.event{top:170px;width:310px;height:325px;background:#fff}
.event .ph{height:195px}
.event p{padding:14px 24px 0;font-size:14px;line-height:22px;color:#222}
.event .meta{position:absolute;left:20px;right:20px;bottom:16px;display:flex;justify-content:space-between;font-size:12px;border-top:1px solid #ddd;padding-top:12px}

/* process */
.process{top:2720px;height:560px}
.process .section-title{top:78px}
.step{top:195px;width:230px;text-align:center}
.step svg{display:block;margin:0 auto}
.step h3{margin-top:24px;font-family:"Roboto",sans-serif;font-weight:500;font-size:17px}
.step p{margin-top:10px;font-size:14px;line-height:24px;color:var(--muted)}
.arrow{top:283px}

/* blog */
.blog{top:3280px;height:560px;background:linear-gradient(180deg,#0d2443,#143559 55%,#0e2444)}
.blog .section-title{top:70px;color:#fff}
.post{top:195px;height:235px;border:3px solid #fff;color:#fff;text-align:center}
.post h3{margin-top:34px;font-family:"Roboto",sans-serif;font-weight:400;font-size:24px}
.post .lede{margin-top:14px;font-size:14px}
.post hr{margin:22px 24px 0;border:0;border-top:3px solid #fff}
.post .date{margin-top:30px;font-size:13px}
.post .btn{position:absolute;left:50%;bottom:-20px;transform:translateX(-50%);width:120px;height:36px;line-height:36px;font-size:14px}

/* subscribe */
.subscribe{top:3840px;height:495px}
.sub-kicker{left:115px;top:128px;color:var(--teal);font-size:22px;letter-spacing:1px}
.sub-title{left:115px;top:165px;font-family:"Roboto",sans-serif;font-weight:400;font-size:36px;line-height:46px}
.sub-form{left:115px;top:300px;width:535px;height:55px;display:flex;box-shadow:0 3px 8px rgba(0,0,0,.25)}
.sub-form .field{flex:1;padding-left:16px;line-height:55px;font-size:14px;color:#888;background:#fff}
.sub-form .go{width:148px;background:var(--teal);color:#fff;font-size:15px;line-height:55px;text-align:center}
.sub-art{left:815px;top:132px;width:260px;height:245px;border-radius:14px;background:linear-gradient(180deg,#e8d9d9 0%,#f1efef 30%,#dfeee4 100%)}

/* contact */
.contact{top:4335px;height:435px;background:linear-gradient(180deg,#23262a,#141618);color:#fff}
.contact h2{left:90px;top:80px;font-size:34px;font-weight:400}
.fld{border-bottom:1px solid #bbb;font-size:15px;height:30px}
.send{left:90px;top:330px;width:84px;height:32px;line-height:32px;text-align:center;background:var(--teal);font-size:15px}
.offices h3{font-size:26px;font-weight:400}
.office{font-size:14px;line-height:22px}
.email-h{left:712px;top:285px;font-size:26px;font-weight:400}
.email{left:712px;top:330px;font-size:14px}

/* footer */
.footer{top:4770px;height:121px;background:var(--teal);color:#fff;text-align:center}
.social{top:34px;left:0;width:100%;display:flex;justify-content:center;gap:14px}
.social span{width:20px;height:20px;background:#fff;border-radius:3px}
.copy{top:72px;width:100%;font-size:13px}
.page-no{right:34px;top:50px;font-size:16px}
</style>
</head>
<body>

<header class="hero">
  <div class="hero-photo" role="img" aria-label="Group of smiling hospitality staff and chefs in uniform"></div>
  <div class="abs brand"><span class="brand-mark"></span><span>BRINDLE<br>PASSAGE</span></div>
  <nav class="abs nav"><span>Welcome</span><span>Destinations</span><span>Contact</span></nav>
  <h1 class="abs hero-title slab">Hospitality Internship Program</h1>
  <div class="abs hero-sub">Culinary - F&amp;B - Front Office - Guest &nbsp;Relations</div>
  <span class="abs btn hero-btn">Get Started Now</span>
</header>

<section class="about">
  <h2 class="abs slab">About us<span>Brindle Passage</span></h2>
  <p class="abs">Hospitality internships are mainly designed for professionals and students in their final university semesters who are looking to learn the ways of working in the growing Chinese market's hospitality industry. The hotels where participants carry out their internships are 4 – 5 star Chinese and international hotels or luxury boutique properties. The program will take place in the most important tourist cities in China, chief among them</p>
  <span class="abs btn">Read More</span>
  <div class="abs about-photo" role="img" aria-label="Hotel receptionists at the front desk"></div>
</section>

<section class="video" role="img" aria-label="Aerial view of a harbour city skyline">
  <svg class="abs play" width="80" height="80" viewBox="0 0 80 80"><circle cx="40" cy="40" r="38" fill="#3a3a3a" fill-opacity=".8"/><path d="M31 24 L58 40 L31 56Z" fill="#fff"/></svg>
</section>

<section class="destinations">
  <h2 class="abs section-title slab">Destinations</h2>
  <div class="abs dest" style="left:90px"><div class="ph" role="img" aria-label="China city skyline at sunset" style="background:linear-gradient(180deg,#d9772e,#8a3d24 60%,#2a1a1a)"></div><div class="lbl">China</div></div>
  <div class="abs dest" style="left:350px"><div class="ph" role="img" aria-label="Spanish city street with historic buildings" style="background:linear-gradient(180deg,#7fa7d0,#b88a55 60%,#5a4030)"></div><div class="lbl">Spain</div></div>
  <div class="abs dest" style="left:610px"><div class="ph" role="img" aria-label="Australian harbour with opera house" style="background:linear-gradient(180deg,#9ab7c8,#6c8a9c 55%,#2f5369)"></div><div class="lbl">Australia</div></div>
  <div class="abs dest" style="left:870px"><div class="ph" role="img" aria-label="Paris glass pyramid and museum courtyard" style="background:linear-gradient(180deg,#e5e2dd,#b9ab96 60%,#8a7b68)"></div><div class="lbl">France</div></div>
</section>

<section class="events">
  <h2 class="abs section-title slab">Events</h2>
  <div class="abs event" style="left:112px"><div class="ph" role="img" aria-label="Hotel rooftop pool at night" style="background:linear-gradient(180deg,#3b3b3b,#3d6a6c 60%,#1d3a3c)"></div><p>Neque porro quisquam est qui dolorem ipsum quia dolor amet, consectetur</p><div class="meta"><span>Dolorem ipsum</span><span>▪ 0 &nbsp;♡ 0</span></div></div>
  <div class="abs event" style="left:445px"><div class="ph" role="img" aria-label="Hotel front desk staff on the phone" style="background:linear-gradient(180deg,#8a6b4c,#c9b49a 60%,#f0ece6)"></div><p>Neque porro quisquam est qui dolorem ipsum quia dolor amet, consectetur</p><div class="meta"><span>Dolorem ipsum</span><span>▪ 0 &nbsp;♡ 0</span></div></div>
  <div class="abs event" style="left:778px"><div class="ph" role="img" aria-label="Hotel staff in uniform in a lobby" style="background:linear-gradient(180deg,#a0743c,#5a3e22 60%,#1f1c1c)"></div><p>Neque porro quisquam est qui dolorem ipsum quia dolor amet, consectetur</p><div class="meta"><span>Dolorem ipsum</span><span>▪ 0 &nbsp;♡ 0</span></div></div>
</section>

<section class="process">
  <h2 class="abs section-title slab">Our Process</h2>
  <svg class="abs arrow" style="left:38px" width="32" height="32" viewBox="0 0 32 32"><circle cx="16" cy="16" r="15" fill="#fff" stroke="#ccc"/><path d="M19 9 L12 16 L19 23" fill="none" stroke="#333" stroke-width="2"/></svg>
  <svg class="abs arrow" style="left:1120px" width="32" height="32" viewBox="0 0 32 32"><circle cx="16" cy="16" r="15" fill="#fff" stroke="#ccc"/><path d="M13 9 L20 16 L13 23" fill="none" stroke="#333" stroke-width="2"/></svg>
  <div class="abs step" style="left:58px">
    <svg width="116" height="116" viewBox="0 0 116 116"><circle cx="58" cy="58" r="55" fill="#fff" stroke="var(--teal)" stroke-width="3"/><rect x="40" y="36" width="32" height="42" fill="none" stroke="var(--teal)" stroke-width="3"/><path d="M46 48h20M46 56h20M46 64h14" stroke="var(--teal)" stroke-width="3"/></svg>
    <h3>APPLY</h3><p>Send your CV for<br>pre-screening.</p></div>
  <div class="abs step" style="left:322px">
    <svg width="116" height="116" viewBox="0 0 116 116"><circle cx="58" cy="58" r="55" fill="#fff" stroke="var(--teal)" stroke-width="3"/><rect x="34" y="40" width="48" height="34" rx="3" fill="none" stroke="var(--teal)" stroke-width="3"/><path d="M34 50h48M40 64h14" stroke="var(--teal)" stroke-width="3"/></svg>
    <h3>DEPOSIT</h3><p>If you are preselected into the program to confirm you are required to pay</p></div>
  <div class="abs step" style="left:595px">
    <svg width="116" height="116" viewBox="0 0 116 116"><circle cx="58" cy="58" r="55" fill="#fff" stroke="var(--teal)" stroke-width="3"/><circle cx="58" cy="58" r="22" fill="none" stroke="var(--teal)" stroke-width="3"/><path d="M66 50c-3-4-14-4-15 1s16 4 15 10-13 5-16 1" fill="none" stroke="var(--teal)" stroke-width="3"/></svg>
    <h3>INTERVIEW</h3><p>We will match with companies that fit your needs and schedule an interview with them.</p></div>
  <div class="abs step" style="left:866px">
    <svg width="116" height="116" viewBox="0 0 116 116"><circle cx="58" cy="58" r="55" fill="#fff" stroke="var(--teal)" stroke-width="3"/><rect x="40" y="34" width="36" height="46" fill="none" stroke="var(--teal)" stroke-width="3"/><circle cx="58" cy="52" r="7" fill="none" stroke="var(--teal)" stroke-width="3"/><path d="M46 68h24" stroke="var(--teal)" stroke-width="3"/></svg>
    <h3>PLACEMENT</h3><p>Acceptance of internship offer. Invitation letter issued.</p></div>
</section>

<section class="blog">
  <h2 class="abs section-title slab">Latest Blog</h2>
  <div class="abs post" style="left:115px;width:435px"><h3>NEQUE PORRO QUISQUAM DOLOREM</h3><div class="lede">Porro quisquam est qui dolorem ipsum quia dolor</div><hr><div class="date">Apr 03, 2023, 7:00 PM &nbsp;San Francisco</div><span class="btn">Read More</span></div>
  <div class="abs post" style="left:617px;width:475px"><h3>DOLOREM IPSUM QUIA DOLOR AMET</h3><div class="lede">Porro quisquam est qui dolorem ipsum quia dolor</div><hr><div class="date">Apr 03, 2023, 7:00 PM &nbsp;San Francisco</div><span class="btn">Read More</span></div>
</section>

<section class="subscribe">
  <div class="abs sub-kicker slab">SUBSCRIBE</div>
  <h2 class="abs sub-title">Sign up for updates on<br>all our future events</h2>
  <div class="abs sub-form"><span class="field">Email Id</span><span class="go">Subscribe Now</span></div>
  <div class="abs sub-art" role="img" aria-label="Illustration of a calendar with a green check mark"></div>
</section>

<section class="contact">
  <h2 class="abs slab">Contact Us</h2>
  <div class="abs fld" style="left:90px;top:160px;width:240px">Name*</div>
  <div class="abs fld" style="left:365px;top:160px;width:245px">Email *</div>
  <div class="abs fld" style="left:90px;top:215px;width:520px">Subject</div>
  <div class="abs fld" style="left:90px;top:270px;width:520px">Message</div>
  <div class="abs send">Send</div>
  <div class="offices">
    <h3 class="abs slab" style="left:712px;top:95px">Our Offices</h3>
    <div class="abs office" style="left:712px;top:150px">Mexico<br>+52 55 0100 4821</div>
    <div class="abs office" style="left:948px;top:150px">Europe<br>+33 7 0102 5566</div>
    <div class="abs office" style="left:712px;top:215px">United States<br>+1 555 010 7742</div>
    <div class="abs office" style="left:948px;top:215px">Australia<br>+61 400 010 288</div>
  </div>
  <h3 class="abs email-h slab">Email</h3>
  <div class="abs email">info@brindle-passage.org</div>
</section>

<footer class="footer">
  <div class="abs social"><span></span><span></span><span></span><span></span></div>
  <div class="abs copy">Copyright © 2016. All Rights Reserved</div>
  <div class="abs page-no">06</div>
</footer>

</body>
</html>
```